Corrimbel Lodge Web Design Project

I am looking for a striking, modern and user friendly site to promote my business, Corrimbel Lodge.

Corrimbel Lodge comprises of 3 elements : Restaurant, Resort and Events and the site must showcase all of these.
Updates

Project Deadline Extended
Reason: Too far away from brief ! Please check out the 2 website links to restaurant sites i LOVE for inspiration ! I am happy to pay for a quality designer and also for anyone that can code this !

Target Market(s)

Our Restaurant clientele demographic is 30-60 years old and are a mix of locals and tourists. The Restaurant is very much a destination venue so we attract people that wish to seek out amazing food.

The Event side of things attracts mainly weddings, this is a lucrative arm of the business and this side of the site must also be outstanding.

The Resort comprises of 7 boutique loft apartment and has a big pool and spa. We attract a mix of locals but want to push it as a ' getaway '

Industry/Entity Type

Business

Requirements
Must have
• I would like the first page to be an overall blog and to highlight the 3 area of the business. Lets have the 3 keywords as clickable tabs that take you to that section of the site.

RESTAURANT RESORT EVENTS

The RESTAURANT page should include the following tabs ( i have provided the information to be added to each tab as an example )

MENU ( Breakfast, Lunch, Dinner, Set Menu, Wine List)

FUNCTIONS (Private Dining Room, Exclusive Use, Wine Nights Coming Soon)

RESERVATIONS (Enquiry Form linked to my info@ address, Reservation Policies, Contact Number)

GALLERY & PRESS ( Press Articles, Latest News, What's On, Photo's, Wedding Hot Spot)

CONTACT US (Opening Times, Map, Contact Details, Sign Up For Our Newsletter, Facebook Link )

The RESORT page should include the following tabs :
# LOFTS & RATES
# FACILITIES
# SPECIAL OFFERS
# GALLERY
# RESERVATIONS

The EVENTS page should include the following tabs :
# WEDDINGS
# CONFERENCES
# PRIVATE EVENTS
# GALLERY
# ENQUIRY FORM
Nice to have
• Include Logo, good branding

```html
<!DOCTYPE html>
<html lang="en">
<head>
<meta charset="utf-8">
<title>Corrimbel Lodge</title>
<link href="https://fonts.googleapis.com/css2?family=Lobster&family=Open+Sans:ital,wght@0,400;0,700;1,400&display=swap" rel="stylesheet">
<style>
:root{
  --cream:#f4efe4;
  --cream-deep:#e6ddcc;
  --band:#dcd5c8;
  --gold:#f2c84b;
  --brown:#6f5b48;
  --brown-soft:#8a7764;
  --text:#6b6259;
  --text-light:#a39a8f;
  --dark-tag:#3a3632;
  --white:#ffffff;
  --paper:#f3f0e9;
}
*{margin:0;padding:0;box-sizing:border-box}
html,body{width:1200px;height:1200px;overflow:hidden}
body{
  position:relative;
  font-family:Arial,Helvetica,sans-serif;
  color:var(--text);
  background:
    radial-gradient(circle at 8% 20%,rgba(255,255,255,.7) 0,rgba(255,255,255,0) 12%),
    radial-gradient(circle at 92% 35%,rgba(255,255,255,.6) 0,rgba(255,255,255,0) 14%),
    radial-gradient(circle at 6% 80%,rgba(255,255,255,.6) 0,rgba(255,255,255,0) 12%),
    radial-gradient(circle at 95% 85%,rgba(255,255,255,.6) 0,rgba(255,255,255,0) 12%),
    linear-gradient(180deg,#efe7d6 0%,#e7dcc6 50%,#eee6d6 100%);
}
.abs{position:absolute}
.top-rule{left:0;top:0;width:1200px;height:3px;background:var(--gold);opacity:.8}

/* hero */
.hero{left:218px;top:0;width:764px;height:390px;overflow:hidden}
.hero-photo{position:absolute;inset:0;
  background:radial-gradient(ellipse at 60% 40%,#f7d89a 0%,#d89b46 45%,#a8692a 80%,#7c4a1f 100%)}
.logo-box{left:315px;top:0;width:170px;height:85px;background:rgba(248,244,236,.93);
  border-radius:0 0 4px 4px;box-shadow:0 2px 4px rgba(0,0,0,.15);
  font-family:'Lobster',cursive;color:#5e5650;font-size:30px;line-height:36px;text-align:center;padding-top:8px}
.nav{left:603px;top:0;height:63px;display:flex}
.nav a{display:block;color:var(--white);font-size:10px;text-decoration:none;padding:40px 0 0;margin-right:24px;height:63px}
.nav a.active{background:rgba(242,200,75,.75);padding:40px 8px 0;margin-right:16px}
.hero-title{left:385px;top:172px;font-family:'Lobster',cursive;font-size:28px;color:var(--white);text-shadow:0 1px 3px rgba(0,0,0,.4)}
.pager{left:536px;top:326px;display:flex;gap:7px}
.pager span{width:22px;height:4px;background:rgba(255,255,255,.75)}
.pager span.on{background:var(--gold)}
.hero-caption{left:218px;top:345px;width:764px;height:45px;background:rgba(225,222,216,.85)}
.hero-caption p{position:absolute;left:121px;top:8px;width:530px;font-size:8px;line-height:9px;color:#6e6962}
.hero-rule{left:315px;top:385px;width:570px;height:4px;background:var(--gold)}

/* sections */
.sections{left:218px;top:390px;width:764px;height:275px;background:rgba(255,255,255,.88)}
.section-card{width:180px}
.section-card h2{font-family:'Lobster',cursive;font-weight:400;font-size:18px;color:var(--brown);height:28px}
.section-card .photo{height:83px;margin-top:4px}
.section-card p{font-size:7.2px;line-height:12px;margin-top:14px;height:70px;color:#6a625a}
.btn-more{display:inline-block;margin-top:12px;height:19px;line-height:19px;padding:0 7px;font-size:7px;color:#8a8178;background:#fff;box-shadow:0 1px 2px rgba(0,0,0,.18)}
.social{left:750px;top:642px;display:flex;gap:9px}
.social span{width:15px;height:15px;border-radius:50%;background:#4d4741}
.dash{height:0;border-top:1px dashed #c9c2b6}

/* blog band */
.blog-band{left:0;top:665px;width:1200px;height:450px;background:rgba(215,209,198,.82)}
.post{width:399px;height:185px;background:var(--paper);border:1px dashed #d4cdc1;box-shadow:0 1px 3px rgba(0,0,0,.08)}
.date-tag{left:-5px;top:13px;width:40px;height:20px;background:var(--dark-tag);color:#fff;font-size:8px;line-height:20px;padding-left:4px}
.comment-count{left:36px;top:13px;width:21px;height:17px;border-radius:50%;background:#aaa38f;color:#fff;font-size:7px;line-height:17px;text-align:center;border:2px solid var(--paper)}
.comment-label{left:28px;top:34px;font-family:'Lobster',cursive;font-size:6px;color:#555}
.post h3{position:absolute;left:72px;top:10px;font-family:'Lobster',cursive;font-weight:400;font-size:22px;color:#5b5752}
.post .sub{left:75px;top:36px;font-style:italic;font-size:8.5px;color:#a29a8e}
.post .body{left:12px;top:65px;width:203px;font-family:'Open Sans',sans-serif;font-size:6.6px;line-height:8.8px;color:#6a645d}
.post .body p+p{margin-top:8px}
.post .frame{left:236px;top:66px;width:149px;height:93px;background:#fff;border:1px dashed #cfc8bc;padding:3px}
.post .frame div{width:100%;height:100%}
.post .credit{left:240px;top:166px;font-style:italic;font-family:'Open Sans',sans-serif;font-size:5.6px;color:#8b847a}
.post .read{left:164px;top:161px;width:53px;height:15px;background:#958d7f;color:#fff;font-size:7.5px;line-height:15px;text-align:center}
.corner{width:10px;height:10px;background:var(--dark-tag)}

.calendar{left:745px;top:707px;width:125px;font-size:9px;text-align:center}
.calendar h4{font-size:13px;color:var(--brown);letter-spacing:.5px;padding-left:11px}
.calendar .month{margin-top:12px;font-size:8.5px;color:#b5ada2;padding-left:0}
.cal-grid{display:grid;grid-template-columns:repeat(7,17.3px);margin-top:4px;font-size:9px;line-height:11.5px;color:#b5aca0}
.cal-grid b{color:#3a3530}
.cal-nav{display:flex;justify-content:space-between;margin-top:8px;font-size:7.5px;font-weight:700;color:var(--brown-soft);width:122px}

.footer-rule{left:315px;top:1115px;width:570px;height:4px;background:var(--gold)}
.footer-logo{left:357px;top:1140px;font-family:'Lobster',cursive;font-size:18px;color:#5b5650}
.footer-copy{left:624px;top:1146px;font-style:italic;font-size:10.5px;color:#5b5650}
</style>
</head>
<body>
<div class="abs top-rule"></div>

<header class="abs hero">
  <div class="hero-photo" role="img" aria-label="Dining hall with long rows of white-clothed tables, wooden chairs and purple flowers"></div>
  <svg class="abs" style="left:78px;top:180px" width="14" height="26" viewBox="0 0 14 26"><path d="M12 2 2 13l10 11" fill="none" stroke="rgba(90,70,50,.6)" stroke-width="3"/></svg>
  <svg class="abs" style="left:669px;top:180px" width="14" height="26" viewBox="0 0 14 26"><path d="M2 2l10 11L2 24" fill="none" stroke="rgba(90,70,50,.6)" stroke-width="3"/></svg>
</header>
<div class="abs logo-box">Place for<br>logo</div>
<nav class="abs nav">
  <a class="active" href="#">Home</a><a href="#">Restaurant</a><a href="#">Resort</a><a href="#">Events</a><a href="#">Contact</a>
</nav>
<div class="abs hero-title">Corrimbel Lodge</div>
<div class="abs pager"><span class="on"></span><span></span><span></span><span></span><span></span></div>
<div class="abs hero-caption"><p>Lorem ipsum dolor sit amet, consectetur adipiscing elit. Suspendisse pulvinar est eget odio porttitor molestie. Vestibulum id dui quis erat vehicula pulvinar. Duis eu felis justo, vitae viverra dui. Pellentesque venenatis mi vel sapien adipiscing venenatis.</p></div>
<div class="abs hero-rule"></div>

<section class="abs sections"></section>
<article class="abs section-card" style="left:315px;top:401px">
  <h2>Restaurant</h2>
  <div class="photo" role="img" aria-label="Bright restaurant room with chandelier, striped chairs and waiter" style="background:linear-gradient(180deg,#e8d3a0 0%,#c59a5e 50%,#8a4a2a 100%)"></div>
  <p>Lorem ipsum dolor sit amet, consectetur adipiscing elit. Suspendisse pulvinar est eget odio porttitor molestie. Vestibulum id dui quis erat vehicula pulvinar. Duis eu felis justo, vitae viverra dui. Pellentesque venenatis mi vel sapien adipiscing venenatis.</p>
  <span class="btn-more">Read more...</span>
</article>
<article class="abs section-card" style="left:513px;top:401px;width:174px">
  <h2>Resort</h2>
  <div class="photo" role="img" aria-label="Hall of set tables with wooden chairs" style="background:linear-gradient(180deg,#efe0c0 0%,#d9a860 55%,#b07a3c 100%)"></div>
  <p>Etiam sodales elit sed urna molestie eget lacinia tellus ullamcorper. Nullam luctus, arcu eget porttitor ullam-corper, mi tellus blandit ante, pulvinar condimentum risus risus bibendum nisi. Donec facilisis eros id arcu posuere laoreet varius lectus porttitor.</p>
  <span class="btn-more" style="padding:0 16px">Read more...</span>
</article>
<article class="abs section-card" style="left:705px;top:401px">
  <h2>Events</h2>
  <div class="photo" role="img" aria-label="Candlelit evening dining table with folded napkins" style="background:radial-gradient(ellipse at 60% 50%,#c8772a 0%,#6a2c10 45%,#1e0c06 100%)"></div>
  <p>Proin luctus, nunc non faucibus luctus, nisl lacus lacinia orci, sed suscipit orci neque vel lorem. Integer egestas velit ut lacus commodo ultricies. Cras et nunc at magna bibendum auctor. Aenean at pellentesque mauris. In sed ante non risus.</p>
  <span class="btn-more" style="padding:0 22px">Read more...</span>
</article>
<div class="abs social" aria-label="Social links"><span></span><span></span><span></span><span></span><span></span></div>
<div class="abs dash" style="left:320px;top:663px;width:565px"></div>

<section class="abs blog-band"></section>

<article class="abs post" style="left:316px;top:683px">
  <div class="abs date-tag">Apr 22</div>
  <div class="abs comment-count">88</div>
  <div class="abs comment-label">comments</div>
  <h3>Blog title goes here</h3>
  <div class="abs sub">The subtitle goes in this line of text in a minor size.</div>
  <div class="abs body">
    <p>Lorem ipsum dolor sit amet, consectetur adipiscing elit. In lobortis erat a felis commodo aliquam placerat ligula pulvi-nar. Etiam nibh metus, rhoncus adipiscing tristique non, gravida at est. Class aptent taciti sociosqu ad litora torquent per conubia nostra, per inceptos himenaeos.</p>
    <p>Vivamus et tellus quis velit blandit ornare. Vivamus diam felis, tincidunt vel vulputate consectetur, ultrices rhoncus tortor.<br>Ut dapibus ante non lectus ornare vehicula fermentum sodales nulla, in fermentum dui pretium non.</p>
  </div>
  <div class="abs frame"><div role="img" aria-label="Restaurant room with chandelier and striped chairs" style="background:linear-gradient(180deg,#e8d3a0 0%,#c59a5e 50%,#8a4a2a 100%)"></div></div>
  <div class="abs credit">Photo courtesy of Corrimbel Lodge</div>
  <div class="abs read">Read More</div>
  <div class="abs corner" style="left:-1px;top:174px;clip-path:polygon(0 0,100% 100%,0 100%)"></div>
  <div class="abs corner" style="left:388px;top:174px;clip-path:polygon(100% 0,100% 100%,0 100%)"></div>
</article>
<div class="abs dash" style="left:316px;top:887px;width:399px"></div>

<article class="abs post" style="left:316px;top:906px">
  <div class="abs date-tag">Apr 22</div>
  <div class="abs comment-count">88</div>
  <div class="abs comment-label">comments</div>
  <h3>Blog title goes here</h3>
  <div class="abs sub">The subtitle goes in this line of text in a minor size.</div>
  <div class="abs body">
    <p>Lorem ipsum dolor sit amet, consectetur adipiscing elit. In lobortis erat a felis commodo aliquam placerat ligula pulvi-nar. Etiam nibh metus, rhoncus adipiscing tristique non, gravida at est. Class aptent taciti sociosqu ad litora torquent per conubia nostra, per inceptos himenaeos.</p>
    <p>Vivamus et tellus quis velit blandit ornare. Vivamus diam felis, tincidunt vel vulputate consectetur, ultrices rhoncus tortor.<br>Ut dapibus ante non lectus ornare vehicula fermentum sodales nulla, in fermentum dui pretium non.</p>
  </div>
  <div class="abs frame"><div role="img" aria-label="Candlelit dining table with flowers and napkins" style="background:radial-gradient(ellipse at 50% 55%,#c8772a 0%,#6a2c10 45%,#1e0c06 100%)"></div></div>
  <div class="abs credit">Photo courtesy of some kind StockPhoto Bank</div>
  <div class="abs read">Read More</div>
  <div class="abs corner" style="left:-1px;top:174px;clip-path:polygon(0 0,100% 100%,0 100%)"></div>
  <div class="abs corner" style="left:388px;top:174px;clip-path:polygon(100% 0,100% 100%,0 100%)"></div>
</article>

<aside class="abs calendar">
  <h4>CALENDAR</h4>
  <div class="month">APRIL2013</div>
  <div class="cal-grid">
    <b>M</b><b>T</b><b>W</b><b>T</b><b>F</b><b>S</b><b>S</b>
    <span></span><span></span><span>1</span><span>2</span><span>3</span><span>4</span><span>5</span>
    <span>6</span><span>7</span><span>8</span><span>9</span><span>10</span><span>11</span><span>12</span>
    <span>13</span><span>14</span><span>15</span><span>16</span><span>17</span><span>18</span><span>19</span>
    <span>20</span><span>21</span><span>22</span><span>23</span><span>24</span><span>25</span><span>26</span>
    <span>27</span><span>28</span><span>29</span><span>30</span><span>31</span>
  </div>
  <div class="cal-nav"><span>&lt; MAR</span><span>MAY &gt;</span></div>
</aside>

<div class="abs footer-rule"></div>
<div class="abs footer-logo">Place for logo</div>
<div class="abs footer-copy">Copyright &nbsp;2013 Corrimbel Lodge</div>
</body>
</html>
```